UPDATE: I have uploaded the selected logo from the other contest, please use it in your designs.

I have a logo design contest as well so not sure how ArtHive handles that. They should integrate at some point. I will describe the overall theme with the logo description. See it for details.

The business card side of it would just build on that same theme.

Target Market(s)

8-40

Industry/Entity Type

Business

Contact Information for Business Card

FirstName LastName
Email

Logo Text

VelMarin

Font styles to use
Sans Serif

Requirements
Must have
• the url VelMarin.com somewhere in it.

```html
<!DOCTYPE html>
<html lang="en">
<head>
<meta charset="utf-8">
<title>VelMarin Business Card</title>
<link href="https://fonts.googleapis.com/css2?family=Lato:wght@400;700;900&display=swap" rel="stylesheet">
<style>
  :root {
    --bg: #e9e9ea;
    --card: #2c2c2d;
    --card-edge: #3a3a3b;
    --pink: #e8188c;
    --blue: #1b75bc;
    --green: #7ab743;
    --white: #ffffff;
    --strip: #f7f7f7;
  }
  * { margin: 0; padding: 0; box-sizing: border-box; }
  html, body {
    width: 1200px; height: 926px; overflow: hidden;
    background: var(--bg);
    font-family: "Lato", sans-serif;
  }
  .sheet {
    position: relative; width: 1200px; height: 926px;
    display: flex; flex-direction: column; align-items: center; justify-content: center; gap: 30px;
  }
  .card {
    position: relative; width: 700px; height: 400px;
    background: radial-gradient(ellipse at 50% 40%, var(--card-edge), var(--card) 70%);
    border-radius: 4px;
    box-shadow: 0 6px 18px rgba(0,0,0,0.25);
    overflow: hidden;
  }

  /* Front */
  .front .blocks { position: absolute; left: 0; top: 140px; }
  .front .block { position: absolute; left: 0; height: 40px; }
  .front .block--pink  { top: 0;  width: 96px; background: var(--pink); }
  .front .block--blue  { top: 40px; width: 130px; background: var(--blue); }
  .front .block--green { top: 80px; width: 96px; background: var(--green); }
  .front .brand {
    position: absolute; left: 170px; right: 60px; top: 160px;
    display: flex; align-items: center; gap: 16px;
  }
  .brand__dot { flex: none; width: 22px; height: 22px; border-radius: 50%; background: var(--green); }
  .brand__name {
    font-weight: 900; font-size: 58px; letter-spacing: 10px;
    color: var(--blue); text-transform: uppercase; line-height: 1;
    white-space: nowrap;
  }

  /* Back */
  .back .logo-strip {
    position: absolute; left: 34px; top: 0; width: 78px; height: 400px;
    background: var(--strip);
    display: flex; align-items: center; justify-content: center;
  }
  .logo-strip__name {
    transform: rotate(-90deg);
    white-space: nowrap;
    font-weight: 900; font-size: 38px; letter-spacing: 8px;
    color: var(--blue); text-transform: uppercase;
  }
  .details { position: absolute; right: 0; top: 150px; width: 410px; }
  .details__band {
    position: relative; height: 42px; margin-left: auto;
    color: var(--white); display: flex; align-items: center;
    padding-left: 24px; font-size: 22px; letter-spacing: 1px;
    white-space: nowrap;
    box-shadow: 0 3px 6px rgba(0,0,0,0.3);
  }
  .details__band--name  { width: 380px; background: var(--pink); font-size: 28px; }
  .details__band--name strong { font-weight: 900; margin-left: 8px; }
  .details__band--web   { width: 395px; background: var(--blue); margin-top: 14px; }
  .details__band--email { width: 410px; background: var(--green); margin-top: 14px; }
</style>
</head>
<body>
<main class="sheet">
  <section class="card front" aria-label="Card front">
    <div class="blocks">
      <div class="block block--pink"></div>
      <div class="block block--blue"></div>
      <div class="block block--green"></div>
    </div>
    <div class="brand">
      <span class="brand__dot"></span>
      <span class="brand__name">VelMarin</span>
    </div>
  </section>

  <section class="card back" aria-label="Card back">
    <div class="logo-strip">
      <span class="logo-strip__name">VelMarin</span>
    </div>
    <div class="details">
      <div class="details__band details__band--name">ALEX <strong>CARTER</strong></div>
      <div class="details__band details__band--web">www.VelMarin.com</div>
      <div class="details__band details__band--email">alexcarter@VelMarin.com</div>
    </div>
  </section>
</main>
</body>
</html>
```